Small business updating business cards

We have already updated our logo via Pixel Forge and downloaded it (hopefully) for you to use. Now an updated set of business cards for Owen Brennan and Stuart Brennan are also needed... we are also hoping that a copy of our outdated business card designs have uploaded successfully as Microsoft Publisher files. Our Strength Through Unity motto has died a slow death so we are hoping to remove it (and other superfluous lingo if the graphic covers the idea) and instead opt for a fancy graphic (?) on the second side of the card that really reflects our desire to obtain product / haulage from Road Transport / Yard Operators and convert legs of their haulage to rail freight where profitable (bulk haulage / containterised etc). Can you help us look larger, bolder and more robust than we really are (two man show)?
Target Market(s)
Transport Industry
Industry/Entity Type
Business
Contact Information for Business Card
Card details for both O Brennan and S Brennan have been uploaded on the publisher files
Colors
Designer to choose colors to be used in the design.
Requirements
Must have
- Similar theme both sides of card
Should not have
- Black on one side white on the other

```html
<!DOCTYPE html>
<html lang="en">
<head>
<meta charset="utf-8">
<title>Corvane Business Card</title>
<link rel="stylesheet" href="https://fonts.googleapis.com/css2?family=Roboto:wght@400;500;700&display=swap">
<style>
  :root {
    --teal: #0a7494;
    --olive: #9a9a2e;
    --white: #ffffff;
    --page: #e8e6e2;
  }
  * { margin: 0; padding: 0; box-sizing: border-box; }
  html, body {
    width: 1200px; height: 1200px; overflow: hidden;
    background: var(--page);
    font-family: "Roboto", Arial, sans-serif;
  }
  .card {
    position: absolute; left: 213px;
    width: 774px; height: 442px;
    overflow: hidden;
    box-shadow: 0 4px 14px rgba(0,0,0,0.25);
  }
  .card--front { top: 150px; background: var(--white); }
  .card--back { top: 633px; background: var(--teal); }
  .card__swoosh { position: absolute; inset: 0; width: 100%; height: 100%; }
  .brand-name {
    position: absolute; font-weight: 700; letter-spacing: -0.5px; line-height: 1;
  }
  .card--front .brand-name { right: 40px; top: 62px; font-size: 56px; color: var(--teal); }
  .card--back .brand-name {
    left: 0; right: 0; top: 170px; text-align: center;
    font-size: 96px; color: var(--white);
  }
  .contact { position: absolute; left: 41px; top: 152px; color: var(--white); }
  .contact__name { font-size: 27px; font-weight: 500; letter-spacing: 0.3px; line-height: 1.1; }
  .contact__role { font-size: 19px; margin-top: 3px; }
  .contact__address { font-size: 19px; line-height: 1.35; margin-top: 26px; }
  .contact__list { list-style: none; margin-top: 14px; }
  .contact__item { display: flex; align-items: center; gap: 8px; height: 28px; }
  .contact__item--primary { font-size: 19px; font-weight: 500; }
  .contact__item--alt { font-size: 16px; }
  .contact__icon { flex: none; }
  .website {
    position: absolute; left: 0; right: 0; top: 384px; text-align: center;
    color: var(--white); font-size: 20px; font-weight: 500; letter-spacing: 0.2px;
  }
</style>
</head>
<body>
  <section class="card card--front">
    <svg class="card__swoosh" viewBox="0 0 774 442" preserveAspectRatio="none" aria-hidden="true">
      <defs>
        <linearGradient id="bandGradient" x1="0" y1="0" x2="1" y2="0">
          <stop offset="0" stop-color="#0a7494"/>
          <stop offset="0.45" stop-color="#5f8a5e"/>
          <stop offset="1" stop-color="#9a9a2e"/>
        </linearGradient>
      </defs>
      <path d="M0,100 Q440,70 774,402 L774,424 Q420,82 0,106 Z" fill="url(#bandGradient)"/>
      <path d="M0,106 Q420,82 774,424 L774,442 L0,442 Z" fill="#0a7494"/>
    </svg>
    <div class="brand-name">Corvane</div>
    <div class="contact">
      <div class="contact__name">STUART BRENNAN</div>
      <div class="contact__role">Director</div>
      <div class="contact__address">14 Carrow Street<br>Bathurst NSW 2795</div>
      <ul class="contact__list">
        <li class="contact__item contact__item--primary">
          <svg class="contact__icon" width="14" height="20" viewBox="0 0 14 20" aria-hidden="true"><rect x="1.5" y="1" width="11" height="18" rx="2" fill="none" stroke="#fff" stroke-width="1.6"/><line x1="5.5" y1="16" x2="8.5" y2="16" stroke="#fff" stroke-width="1.4"/></svg>
          0400 555 012
        </li>
        <li class="contact__item contact__item--primary">
          <svg class="contact__icon" width="17" height="12" viewBox="0 0 17 12" aria-hidden="true"><rect x="0.75" y="0.75" width="15.5" height="10.5" fill="none" stroke="#fff" stroke-width="1.3"/><path d="M0.75,0.75 L8.5,7 L16.25,0.75" fill="none" stroke="#fff" stroke-width="1.3"/></svg>
          brennans@corvane.com.au
        </li>
        <li class="contact__item contact__item--alt">
          <svg class="contact__icon" width="17" height="12" viewBox="0 0 17 12" aria-hidden="true"><rect x="0.75" y="0.75" width="15.5" height="10.5" fill="none" stroke="#fff" stroke-width="1.3"/><path d="M0.75,0.75 L8.5,7 L16.25,0.75" fill="none" stroke="#fff" stroke-width="1.3"/></svg>
          corvane@mailbox.com (Alternate)
        </li>
        <li class="contact__item contact__item--alt">
          <svg class="contact__icon" width="17" height="12" viewBox="0 0 17 12" aria-hidden="true"><rect x="0.75" y="0.75" width="15.5" height="10.5" fill="none" stroke="#fff" stroke-width="1.3"/><path d="M0.75,0.75 L8.5,7 L16.25,0.75" fill="none" stroke="#fff" stroke-width="1.3"/></svg>
          corvane@inboxmail.com (Alternate)
        </li>
      </ul>
    </div>
  </section>

  <section class="card card--back">
    <div class="brand-name">Corvane</div>
    <div class="website">www.corvane.com.au</div>
  </section>
</body>
</html>
```